Concierge Healthcare Business Card Design and Logo

We need a logo and business card design for a new company called "Sound Keeper". We will provide concierge audiological care, hearing aids, hearing exams, custom hearing protection etc to patients in the comfort of their homes and offices. We would like a sleek and modern design preferably with an Ear related logo.

Target Market(s)

People with hearing loss, Hunters, Musicians
My usual clientele are older individuals so usually 50+ years old

Industry/Entity Type

Health Care

Contact Information for Business Card

Clara Whitfield, AuD
Audiologist
512-418-2967
soundkeeper@mailvista.net
www.soundkeeperclinic.net

Logo Text

Sound Keeper

Number of Pages Required

3 page

```html
<!DOCTYPE html>
<html lang="en">
<head>
<meta charset="utf-8">
<title>Sound Keeper — Business Card</title>
<link rel="stylesheet" href="https://fonts.googleapis.com/css2?family=Source+Sans+3:wght@400;600&family=Questrial&display=swap">
<style>
  :root {
    --brand-orange: #f28a1d;
    --brand-grey: #7a7a7a;
    --card-white: #ffffff;
    --ink-light: #ffffff;
    --backdrop: #ececec;
    --card-shadow: 0 6px 18px rgba(0, 0, 0, 0.12);
  }
  * { margin: 0; padding: 0; box-sizing: border-box; }
  html, body {
    width: 1200px;
    height: 900px;
    overflow: hidden;
    background: var(--backdrop);
  }
  .canvas {
    position: relative;
    width: 1200px;
    height: 900px;
  }
  .card {
    position: absolute;
    box-shadow: var(--card-shadow);
  }
  /* Front: contact side */
  .card-front {
    left: 238px;
    top: 62px;
    width: 555px;
    height: 342px;
    background: var(--brand-orange);
    color: var(--ink-light);
    font-family: "Source Sans 3", "Myriad Pro", sans-serif;
  }
  .person-name {
    position: absolute;
    left: 33px;
    top: 67px;
    font-size: 21px;
    font-weight: 600;
    line-height: 1;
  }
  .person-role {
    position: absolute;
    left: 33px;
    top: 92px;
    font-size: 15px;
    line-height: 1;
  }
  .address {
    position: absolute;
    left: 33px;
    top: 167px;
    font-size: 15px;
    font-style: normal;
    line-height: 20px;
  }
  .contact-list {
    position: absolute;
    left: 33px;
    top: 216px;
    list-style: none;
    font-size: 15px;
    line-height: 20px;
  }
  .contact-item {
    display: flex;
    align-items: center;
    gap: 9px;
  }
  .contact-icon {
    width: 12px;
    height: 12px;
    flex: none;
    fill: var(--ink-light);
  }
  .front-wordmark {
    position: absolute;
    left: 285px;
    top: 150px;
    font-family: "Questrial", sans-serif;
    font-size: 34px;
    color: var(--ink-light);
    white-space: nowrap;
  }
  /* Back: brand side */
  .card-back {
    left: 457px;
    top: 518px;
    width: 560px;
    height: 344px;
    background: var(--card-white);
  }
  .back-brand {
    position: absolute;
    left: 0;
    right: 0;
    top: 210px;
    display: flex;
    justify-content: center;
    align-items: center;
    gap: 14px;
  }
  .brand-dot {
    width: 22px;
    height: 22px;
    border-radius: 50%;
    background: var(--brand-orange);
  }
  .back-wordmark {
    font-family: "Questrial", sans-serif;
    font-size: 40px;
    color: var(--brand-grey);
    line-height: 1;
  }
</style>
</head>
<body>
<main class="canvas">
  <section class="card card-front" aria-label="Business card, contact side">
    <h1 class="person-name">Clara Whitfield, AuD</h1>
    <p class="person-role">Audiologist</p>
    <address class="address">
      2100 Cedar Ridge Drive<br>
      Austin, TX 78704.
    </address>
    <ul class="contact-list">
      <li class="contact-item">
        <svg class="contact-icon" viewBox="0 0 12 12" aria-hidden="true"><path d="M2.4 0.6 L4.3 2.8 L3.4 4.2 C4.1 5.7 6.3 7.9 7.8 8.6 L9.2 7.7 L11.4 9.6 L10.2 11.3 C5.6 11.6 0.4 6.4 0.7 1.8 Z"/></svg>
        <span>512-418-2967</span>
      </li>
      <li class="contact-item">
        <svg class="contact-icon" viewBox="0 0 12 12" aria-hidden="true"><path d="M1 3 H11 V10 H1 Z M1.6 3.4 L6 7 L10.4 3.4" fill="var(--ink-light)" stroke="var(--brand-orange)" stroke-width="0.9"/></svg>
        <span>soundkeeper@mailvista.net</span>
      </li>
      <li class="contact-item">
        <svg class="contact-icon" viewBox="0 0 12 12" aria-hidden="true"><circle cx="6" cy="6" r="5.5"/><path d="M3 3.5 C4.5 4 4.2 6 5.5 6.5 C6.5 7 6 9 7 10 M7.5 2 C8 3.5 9.5 4 10.5 4.5" fill="none" stroke="var(--brand-orange)" stroke-width="1"/></svg>
        <span>www.soundkeeperclinic.net</span>
      </li>
    </ul>
    <p class="front-wordmark">Sound Keeper</p>
  </section>

  <section class="card card-back" aria-label="Business card, brand side">
    <div class="back-brand">
      <span class="brand-dot" aria-hidden="true"></span>
      <p class="back-wordmark">Sound Keeper</p>
    </div>
  </section>
</main>
</body>
</html>
```